Willowmere Haven tri-fold brochure

We are a small assisted living in a home-like environment. Brochure should be warm, heartfelt and include the list of services we provide (see existing brochure). I also want the front picture replaced with stock photo (so no picture of owners). New name to use (instead of Hester) is Dorian Feltrowe, and email is feltrowe@quintmail.example. Address is same. If you can find better photos, that would be good, all the photos here are dated. We are looking for a more professional design that still conveys warmth, because we are in a home-setting and only care for 9 residents.

Target Market(s)

35-55 year old children looking for an assisted living because their parents are unable to care for them.

Industry/Entity Type

Environment

Contact Information for Business Card

Dorian Feltrowe
Willowmere Haven or Willowmere Haven Assisted Living
40718 Pinegrove Ln. Conroe, TX 77519
281-647-5192

Requirements
Must have
• List of services offered (feel free to re-word or add/change)
• Be sure to change "Hester/Hestie" to Dorian / Dorian Feltrowe

```html
<!DOCTYPE html>
<html lang="en">
<head>
<meta charset="utf-8">
<title>Willowmere Haven — Tri-fold Brochure</title>
<link href="https://fonts.googleapis.com/css2?family=Lato:ital,wght@0,300;0,400;0,700;1,400&display=swap" rel="stylesheet">
<style>
  :root{
    --teal:#5fb8b4;
    --teal-dark:#4aa5a1;
    --rose:#c9647a;
    --rose-text:#d0667c;
    --ink:#444a4f;
    --paper:#ffffff;
    --card:#f6f6f6;
    --stage:#7d7d7d;
    --rule:#d9d9d9;
  }
  *{box-sizing:border-box;margin:0;padding:0}
  html,body{width:1200px;height:1200px;overflow:hidden;background:var(--stage)}
  body{font-family:"Lato",Arial,sans-serif;color:var(--ink)}

  .brochure{position:absolute;left:30px;top:160px;width:1140px;height:880px;display:flex;box-shadow:0 10px 30px rgba(0,0,0,.25)}
  .panel{position:relative;width:380px;height:100%;overflow:hidden;background:var(--paper)}
  .panel + .panel{border-left:1px solid #e4e4e4}

  /* colour bands */
  .panel--testimonials{background:linear-gradient(var(--teal) 0 56%, var(--rose) 56% 100%)}
  .panel--story{background:linear-gradient(var(--teal) 0 40px, var(--paper) 40px calc(100% - 56px), var(--rose) calc(100% - 56px))}
  .panel--cover{background:linear-gradient(var(--teal) 0 72%, var(--rose) 72% 100%)}

  .card{position:absolute;background:var(--card)}
  .panel--testimonials .card{inset:40px 0 44px 24px;border-radius:24px 0 0 24px}
  .panel--story .card{inset:60px 0 80px 0}
  .panel--cover .card{inset:40px 40px 60px 0;border-radius:0 0 28px 0}

  /* testimonials */
  .tab{position:absolute;top:60px;left:110px;width:230px;height:42px;background:var(--teal);border-radius:21px 6px 21px 6px;color:#fff;font-style:italic;font-size:28px;display:flex;align-items:center;justify-content:center}
  .testimonial-block{position:absolute;left:60px;right:24px;text-align:center;font-style:italic;font-size:14.5px;line-height:1.35}
  .quote{color:var(--teal)}
  .mark{color:var(--rose);font-style:normal;font-weight:700;font-size:20px;line-height:0;vertical-align:-4px;margin:0 4px}
  .intro{top:122px}
  .found{top:176px}
  .facility{top:232px}
  .outro{top:575px;left:48px;right:18px;font-size:14px}
  .outro p{margin-bottom:4px}
  .refs{color:var(--teal)}

  .photo{position:absolute}
  .photo--couple-beach{left:40px;top:380px;width:190px;height:140px;background:linear-gradient(135deg,#9cc4d6,#d9b99a 60%,#a27a62);transform:rotate(-3deg)}
  .photo--park{left:200px;top:395px;width:180px;height:150px;background:linear-gradient(160deg,#cfe6b0,#6da85a 55%,#3f7a3a);clip-path:polygon(0 0,100% 18%,82% 100%,8% 92%)}

  /* story panel */
  .headline{position:absolute;top:88px;left:0;right:0;text-align:center;color:var(--rose-text);font-weight:400;font-size:23px;line-height:1.2}
  .divider{position:absolute;left:60px;right:60px;height:1px;background:var(--rule)}
  .promise{position:absolute;top:164px;left:20px;right:20px;text-align:center;color:var(--teal);font-size:22px;line-height:1.18}
  .services{position:absolute;top:258px;left:30px;right:30px}
  .services h3{text-align:center;color:var(--rose-text);font-weight:700;font-size:15px;letter-spacing:.5px;margin-bottom:6px}
  .services ul{list-style:none;display:grid;grid-template-columns:1fr 1fr;column-gap:14px;row-gap:3px;font-size:13px;line-height:1.3}
  .services li{display:flex;align-items:center;gap:6px}
  .services svg{width:12px;height:12px;flex:none}
  .photo--embrace{left:60px;top:362px;width:300px;height:158px;background:linear-gradient(150deg,#eef1f4,#d8cfc4 55%,#b8a48f);clip-path:polygon(12% 0,100% 0,100% 100%,0 100%)}
  .invite{position:absolute;top:540px;left:10px;right:10px;text-align:center;color:var(--rose-text);font-size:22px;line-height:1.18}
  .contact{position:absolute;top:665px;left:0;right:0;text-align:center;font-style:normal;font-size:19px;line-height:1.25;color:var(--ink)}
  .contact .email{color:var(--teal);font-size:17px}

  /* cover panel */
  .photo--cover{left:30px;top:55px;width:300px;height:300px;border-radius:50%;background:radial-gradient(circle at 40% 35%,#f1e6dc,#c9b7a6 45%,#5e8eb0 80%);box-shadow:0 6px 0 -1px #e2e2e2}
  .brand{position:absolute;top:395px;left:0;right:40px;text-align:center;color:var(--teal);font-weight:300;font-size:46px;line-height:1.05}
  .service{position:absolute;top:518px;left:0;right:40px;text-align:center;color:var(--rose-text);font-weight:700;font-size:20px}
  .tagline{position:absolute;top:556px;left:10px;right:50px;text-align:center;font-size:16px;line-height:1.3}
  .owner{position:absolute;top:660px;left:0;right:40px;text-align:center;color:var(--teal);font-weight:700;font-size:21px}
  .phone{position:absolute;top:692px;left:0;right:40px;display:flex;justify-content:center;align-items:center;gap:10px;font-weight:700;font-size:30px;color:var(--ink)}
  .phone svg{width:26px;height:26px}
</style>
</head>
<body>
<main class="brochure">

  <section class="panel panel--testimonials">
    <div class="card"></div>
    <div class="tab">Testimonials</div>
    <p class="testimonial-block intro">My mom lived in five private care homes.<br>When she moved here she said:</p>
    <p class="testimonial-block found"><span class="mark">“</span><span class="quote">"I've finally found<br>my home!"</span><span class="mark">”</span></p>
    <p class="testimonial-block facility"><span class="mark">“</span>I lived in a facility where everything seemed to be....door.....,door......,door......<br>Here is small, familiar<br>and comfortable<span class="mark">”</span></p>
    <div class="photo photo--couple-beach" role="img" aria-label="Smiling senior couple outdoors by the sea"></div>
    <div class="photo photo--park" role="img" aria-label="Caregiver walking with a resident in a wheelchair through a sunny park"></div>
    <div class="testimonial-block outro">
      <p><span class="mark">“</span><span class="quote">I'd be miserable in a nursing home!</span><span class="mark">”</span><br>If you are one of the millions of people<br>who feel this way, we say,</p>
      <p><span class="mark">“</span><span class="quote">Trust your instincts</span><span class="mark">”</span></p>
      <p>Discover that smaller is better where<br>full service care is provided in a real home.</p>
      <p class="refs">References Available</p>
    </div>
  </section>

  <section class="panel panel--story">
    <div class="card"></div>
    <h2 class="headline">Smaller is better<br>when it comes to the elderly</h2>
    <div class="divider" style="top:154px"></div>
    <p class="promise">Our unique homes are designed to make the surroundings familiar and the care consistent</p>
    <div class="services">
      <h3>Our Services</h3>
      <ul>
        <li><svg viewBox="0 0 12 12" aria-hidden="true"><path d="M2 6.5l2.5 2.5L10 3.5" fill="none" stroke="#5fb8b4" stroke-width="2"/></svg>Personal care &amp; bathing</li>
        <li><svg viewBox="0 0 12 12" aria-hidden="true"><path d="M2 6.5l2.5 2.5L10 3.5" fill="none" stroke="#5fb8b4" stroke-width="2"/></svg>Medication management</li>
        <li><svg viewBox="0 0 12 12" aria-hidden="true"><path d="M2 6.5l2.5 2.5L10 3.5" fill="none" stroke="#5fb8b4" stroke-width="2"/></svg>Home-cooked meals</li>
        <li><svg viewBox="0 0 12 12" aria-hidden="true"><path d="M2 6.5l2.5 2.5L10 3.5" fill="none" stroke="#5fb8b4" stroke-width="2"/></svg>Memory care support</li>
        <li><svg viewBox="0 0 12 12" aria-hidden="true"><path d="M2 6.5l2.5 2.5L10 3.5" fill="none" stroke="#5fb8b4" stroke-width="2"/></svg>Housekeeping &amp; laundry</li>
        <li><svg viewBox="0 0 12 12" aria-hidden="true"><path d="M2 6.5l2.5 2.5L10 3.5" fill="none" stroke="#5fb8b4" stroke-width="2"/></svg>24-hour supervision</li>
      </ul>
    </div>
    <div class="photo photo--embrace" role="img" aria-label="Happy senior couple embracing at home"></div>
    <p class="invite">Please call for personal tour and experience the Willowmere Haven difference</p>
    <div class="divider" style="top:648px"></div>
    <address class="contact">
      40718 Pinegrove Ln.<br>Conroe, Texas<br>
      <span class="email">feltrowe@quintmail.example</span>
    </address>
  </section>

  <section class="panel panel--cover">
    <div class="card"></div>
    <div class="photo photo--cover" role="img" aria-label="Caregiver smiling with a senior resident in a blue sweater"></div>
    <h1 class="brand">Willowmere<br>Haven</h1>
    <p class="service">Assisted Living &amp; Memory Care</p>
    <p class="tagline">Offering a true and noble commitment to the highest standards of care in the industry</p>
    <div class="divider" style="top:645px;left:50px;right:90px"></div>
    <p class="owner">Dorian Feltrowe</p>
    <p class="phone">
      <svg viewBox="0 0 24 24" aria-hidden="true"><rect width="24" height="24" rx="5" fill="#c9647a"/><path d="M8.2 5.5c.5 0 .8.3 1 .8l.9 2.3c.2.5 0 1-.4 1.3l-.9.7c.7 1.6 1.9 2.8 3.5 3.5l.7-.9c.3-.4.8-.6 1.3-.4l2.3.9c.5.2.8.5.8 1v1.8c0 .8-.6 1.5-1.5 1.5C10.3 18.8 5.2 13.7 5.2 7.2c0-.9.7-1.5 1.5-1.5z" fill="#fff"/></svg>
      281-647-5192
    </p>
  </section>

</main>
</body>
</html>
```